Powerpoint template

I am looking for a brand based PPT template that can also be used as the basis for datasheet creation. I have attached a document with some of our branding structure in as an FYI to help.

To be clear I am looking a background design, bullets, layouts, different styles for differing content types. This is a template to be used for lots of presentations.
Updates

Project Deadline Extended
Reason: I have committed to the payment and wanted to give people chance to respond.

Target Market(s)

Enterprise

Requirements
Must have
• Brand standard. different page design choices for different content types
Nice to have
• brand font if it works. Use of some play on the logo in bullets
Should not have
• must be on brand and focused on the business audience

```html
<!DOCTYPE html>
<html lang="en">
<head>
<meta charset="utf-8">
<title>vectralink – Presentation Template</title>
<link href="https://fonts.googleapis.com/css2?family=Open+Sans:ital,wght@0,400;0,600;0,700;1,400&display=swap" rel="stylesheet">
<style>
:root{
  --stage:#000000;
  --paper:#ffffff;
  --brand-green:#7ab532;
  --brand-blue:#1d6fa3;
  --deep-blue:#0b3765;
  --mid-blue:#155d93;
  --body-text:#4a4a4a;
  --placeholder:#d3d1c2;
  --placeholder-glow:#f4f3ea;
  --footer-text:#ffffff;
}
*{box-sizing:border-box;margin:0;padding:0}
html,body{width:1200px;height:1000px;overflow:hidden;background:var(--stage)}
body{position:relative;font-family:"Open Sans",Arial,sans-serif;color:var(--body-text)}

.slide{position:absolute;width:500px;height:375px;background:var(--paper);overflow:hidden}
.slide--title{left:40px;top:67px}
.slide--two-col{left:637px;top:67px}
.slide--three-col{left:40px;top:526px}
.slide--fading{left:637px;top:526px}

.wave{position:absolute;left:0;top:0;width:500px;height:375px}

.slide-heading{position:absolute;left:33px;top:14px;font-size:26px;font-weight:700;color:var(--brand-green);letter-spacing:-.2px}
.slide-heading--centered{left:0;right:0;text-align:center}
.heading-rule{position:absolute;left:80px;right:50px;top:64px;height:8px;
  background:radial-gradient(ellipse at 50% 0,rgba(0,0,0,.18),rgba(0,0,0,0) 70%)}

.brand{position:absolute;display:flex;align-items:center;gap:6px;font-weight:400;letter-spacing:-.3px}
.brand__dot{border-radius:50%;display:block}
.brand--hero{left:147px;top:92px;font-size:30px;color:var(--brand-blue)}
.brand--hero .brand__dot{width:40px;height:40px;background:var(--brand-green)}
.brand--footer{right:4px;font-size:19px;color:var(--footer-text)}
.brand--footer .brand__dot{width:22px;height:22px;border:2px solid var(--footer-text)}

.hero-title{position:absolute;left:0;right:0;top:245px;text-align:center;font-size:31px;color:#fff;font-weight:400}
.hero-year{position:absolute;left:0;right:0;top:287px;text-align:center;font-size:10px;font-style:italic;color:#b9d3e6}

.pager{position:absolute;right:22px;display:flex;align-items:center;gap:8px;font-size:9px;color:#fff}
.pager i{font-style:italic;font-weight:700}
.pager__btn{width:18px;height:12px;border-radius:6px;background:rgba(255,255,255,.14);display:flex;align-items:center;justify-content:center}
.pager__btn svg{width:6px;height:7px}

.footer-address{position:absolute;left:18px;font-size:6.2px;line-height:8.5px;color:var(--footer-text)}
.contact{position:absolute;display:flex;align-items:center;gap:7px;font-size:6.2px;color:var(--footer-text)}
.contact__icon{width:14px;height:14px;border-radius:50%;background:rgba(255,255,255,.16);display:flex;align-items:center;justify-content:center}
.contact__icon svg{width:8px;height:8px}

.body-copy{position:absolute;font-size:9.3px;line-height:12.6px;text-align:justify;color:var(--body-text)}
.bullet-list{list-style:none}
.bullet-list li{position:relative;margin-bottom:10px}
.bullet-list li::before{content:"";position:absolute;left:-17px;top:3px;border-left:6px solid #333;border-top:3.5px solid transparent;border-bottom:3.5px solid transparent}
.bullet-list--compact{font-size:8.4px;line-height:10px}
.bullet-list--compact li{margin-bottom:15px}
.bullet-list--compact li::before{top:2px}
.lead-copy{font-size:8.4px;line-height:12.4px;text-align:left}
.caption{font-style:italic;color:#555}

.shadow{position:absolute;height:10px;background:radial-gradient(ellipse at 50% 0,rgba(0,0,0,.28),rgba(0,0,0,0) 70%)}

.picture-slot{position:absolute;width:130px;height:62px;
  background:radial-gradient(ellipse at 50% 45%,var(--placeholder-glow) 0,var(--placeholder) 60%);
  display:flex;align-items:center;justify-content:center;font-size:6px;font-weight:700;color:#333}
.picture-slot--flat{background:var(--placeholder)}
.feature-icon{position:absolute;width:12px;height:12px}
</style>
</head>
<body>

<!-- Title slide -->
<section class="slide slide--title">
  <div class="brand brand--hero"><span class="brand__dot"></span>vectralink</div>
  <svg class="wave" viewBox="0 0 500 375" aria-hidden="true">
    <defs>
      <linearGradient id="heroSea" x1="0" y1="0" x2="0" y2="1">
        <stop offset="0" stop-color="#2fa2cf"/>
        <stop offset=".45" stop-color="#1a6fa5"/>
        <stop offset="1" stop-color="#0b3765"/>
      </linearGradient>
      <radialGradient id="heroRays" cx=".45" cy=".1" r=".6">
        <stop offset="0" stop-color="#ffffff" stop-opacity=".35"/>
        <stop offset="1" stop-color="#ffffff" stop-opacity="0"/>
      </radialGradient>
    </defs>
    <path d="M0 175 C120 180 200 200 280 205 C360 210 430 205 500 205 L500 375 L0 375Z" fill="url(#heroSea)"/>
    <path d="M0 175 C120 180 200 200 280 205 C360 210 430 205 500 205 L500 375 L0 375Z" fill="url(#heroRays)"/>
  </svg>
  <h1 class="hero-title">The Presentation Title</h1>
  <p class="hero-year">2014</p>
  <div class="pager" style="top:341px"><span>1</span><i>of</i><span>13</span>
    <span class="pager__btn"><svg viewBox="0 0 6 7"><path d="M1 0.5 L5 3.5 L1 6.5" fill="none" stroke="#fff" stroke-width="1.4"/></svg></span>
  </div>
</section>

<!-- Two columns slide -->
<section class="slide slide--two-col">
  <h2 class="slide-heading slide-heading--centered">Two Columns Big Picture Example</h2>
  <div class="heading-rule"></div>
  <ul class="body-copy bullet-list bullet-list--compact" style="left:23px;top:99px;width:167px">
    <li>consetetur sadipscing elitr, sed diam nonumy eirmod tempor invidunt ut labore et dolore magna aliquyam erat, sed diam voluptua.</li>
    <li>Stet clita kasd gubergren, no sea takimata sanctus est Lorem ipsum dolor sit amet. Lorem ipsum dolor sit amet, consetetur sadipscing elitr, sed diam nonumy eirmod tempor invidunt ut labore et dolore dolores et ea rebum. Stet clita kasd gubergren, no sea takimata sanctus est Lorem ipsum dolor sit amet.</li>
  </ul>
  <p class="body-copy lead-copy" style="left:24px;top:257px;width:222px">Lorem ipsum dolor sit amet consetetur sadipscing dolore magna aliquyam erat, sed diam voluptua. Lorem ipsum dolor sit amet consetetur sadipscing dolore magna aliquyam erat, sed diam voluptua</p>
  <div class="shadow" style="left:320px;top:212px;width:110px"></div>
  <p class="body-copy caption" style="left:273px;top:230px;width:194px;font-size:8.4px;line-height:11.8px">Lorem ipsum dolor sit amet consetetur sadipscing dolore magna aliquyam erat, sed diam voluptua.</p>

  <svg class="wave" viewBox="0 0 500 375" aria-hidden="true">
    <defs>
      <linearGradient id="footSea2" x1="0" y1="0" x2="0" y2="1">
        <stop offset="0" stop-color="#1d6fa3"/><stop offset="1" stop-color="#0b3765"/>
      </linearGradient>
    </defs>
    <path d="M0 310 C100 324 200 322 280 304 C360 286 430 270 500 266 L500 375 L0 375Z" fill="url(#footSea2)"/>
  </svg>
  <div class="brand brand--footer" style="top:279px"><span class="brand__dot"></span>vectralink</div>
  <p class="footer-address" style="top:332px">Lorem Ipsum Street 122<br>State, Country<br>Phone&nbsp; 0123 4567 89</p>
  <div class="contact" style="left:113px;top:334px"><span class="contact__icon"><svg viewBox="0 0 8 8"><circle cx="4" cy="4" r="2.2" fill="#fff"/></svg></span>social-one.example/company</div>
  <div class="contact" style="left:113px;top:358px"><span class="contact__icon"><svg viewBox="0 0 8 8"><circle cx="4" cy="4" r="2.8" fill="none" stroke="#fff" stroke-width="1.1"/></svg></span>hello@company-name.com</div>
  <div class="contact" style="left:262px;top:306px"><span class="contact__icon"><svg viewBox="0 0 8 8"><path d="M1 4.2 L4 1.5 L7 4.2 V7 H1Z" fill="#fff"/></svg></span>company-name.com</div>
  <div class="contact" style="left:262px;top:331px"><span class="contact__icon"><svg viewBox="0 0 8 8"><rect x="1.5" y="1.5" width="5" height="5" fill="#fff"/></svg></span>social-two.example/company</div>
  <div class="contact" style="left:262px;top:356px"><span class="contact__icon"><svg viewBox="0 0 8 8"><path d="M2 1.5 L6.5 4 L2 6.5Z" fill="#fff"/></svg></span>video-hub.example/company</div>
  <div class="pager" style="top:341px">
    <span class="pager__btn"><svg viewBox="0 0 6 7"><path d="M5 0.5 L1 3.5 L5 6.5" fill="none" stroke="#fff" stroke-width="1.4"/></svg></span>
    <span>2</span><i>of</i><span>13</span>
    <span class="pager__btn"><svg viewBox="0 0 6 7"><path d="M1 0.5 L5 3.5 L1 6.5" fill="none" stroke="#fff" stroke-width="1.4"/></svg></span>
  </div>
</section>

<!-- Three columns slide -->
<section class="slide slide--three-col">
  <h2 class="slide-heading">Three Columns Example</h2>
  <div class="heading-rule"></div>
  <div class="picture-slot" style="left:33px;top:89px" role="img" aria-label="Column one image"></div>
  <div class="picture-slot" style="left:185px;top:89px" role="img" aria-label="Column two image"></div>
  <div class="picture-slot" style="left:336px;top:89px" role="img" aria-label="Column three image"></div>
  <div class="shadow" style="left:38px;top:152px;width:120px"></div>
  <div class="shadow" style="left:190px;top:152px;width:120px"></div>
  <div class="shadow" style="left:341px;top:152px;width:120px"></div>
  <p class="body-copy" style="left:33px;top:168px;width:130px">Stet clita kasd gubergren, no sea takimata sanctus est Lorem ipsum dolor sit amet. Consetetur labore et dolore dolores et ea rebum.<br><br>Stet clita kasd gubergren, no sea takimata sanctus est Lorem ipsum dolor sit amet.</p>
  <p class="body-copy" style="left:185px;top:168px;width:130px">Stet clita kasd gubergren, no sea takimata sanctus est Lorem ipsum dolor sit amet, consetetur labore et dolore dolores et ea rebum.<br><br>Stet clita kasd gubergren, no sea takimata sanctus est Lorem ipsum dolor sit amet.</p>
  <p class="body-copy" style="left:336px;top:168px;width:130px">Stet clita kasd gubergren, no sea takimata sanctus est Lorem ipsum dolor sit amet.<br><br>Stet clita kasd gubergren, no sea takimata sanctus est Lorem ipsum dolor sit amet.</p>

  <svg class="wave" viewBox="0 0 500 375" aria-hidden="true">
    <defs>
      <linearGradient id="footSea3" x1="0" y1="0" x2="0" y2="1">
        <stop offset="0" stop-color="#1d6fa3"/><stop offset="1" stop-color="#0b3765"/>
      </linearGradient>
    </defs>
    <path d="M0 310 C100 324 200 322 280 304 C360 286 430 270 500 266 L500 375 L0 375Z" fill="url(#footSea3)"/>
  </svg>
  <div class="brand brand--footer" style="top:279px"><span class="brand__dot"></span>vectralink</div>
  <p class="footer-address" style="top:332px">Lorem Ipsum Street 122<br>State, Country<br>Phone&nbsp; 0123 4567 89</p>
  <div class="contact" style="left:113px;top:334px"><span class="contact__icon"><svg viewBox="0 0 8 8"><circle cx="4" cy="4" r="2.2" fill="#fff"/></svg></span>social-one.example/company</div>
  <div class="contact" style="left:113px;top:358px"><span class="contact__icon"><svg viewBox="0 0 8 8"><circle cx="4" cy="4" r="2.8" fill="none" stroke="#fff" stroke-width="1.1"/></svg></span>hello@company-name.com</div>
  <div class="contact" style="left:262px;top:306px"><span class="contact__icon"><svg viewBox="0 0 8 8"><path d="M1 4.2 L4 1.5 L7 4.2 V7 H1Z" fill="#fff"/></svg></span>company-name.com</div>
  <div class="contact" style="left:262px;top:331px"><span class="contact__icon"><svg viewBox="0 0 8 8"><rect x="1.5" y="1.5" width="5" height="5" fill="#fff"/></svg></span>social-two.example/company</div>
  <div class="contact" style="left:262px;top:356px"><span class="contact__icon"><svg viewBox="0 0 8 8"><path d="M2 1.5 L6.5 4 L2 6.5Z" fill="#fff"/></svg></span>video-hub.example/company</div>
  <div class="pager" style="top:341px">
    <span class="pager__btn"><svg viewBox="0 0 6 7"><path d="M5 0.5 L1 3.5 L5 6.5" fill="none" stroke="#fff" stroke-width="1.4"/></svg></span>
    <span>3</span><i>of</i><span>13</span>
    <span class="pager__btn"><svg viewBox="0 0 6 7"><path d="M1 0.5 L5 3.5 L1 6.5" fill="none" stroke="#fff" stroke-width="1.4"/></svg></span>
  </div>
</section>

<!-- Fading content slide -->
<section class="slide slide--fading">
  <h2 class="slide-heading">Fading Content Example</h2>
  <div class="heading-rule"></div>
  <div class="picture-slot picture-slot--flat" style="left:33px;top:89px" role="img" aria-label="Picture placeholder">PLACE YOUR PICTURE HERE</div>
  <div class="picture-slot picture-slot--flat" style="left:33px;top:160px" role="img" aria-label="Picture placeholder">PLACE YOUR PICTURE HERE</div>
  <div class="picture-slot picture-slot--flat" style="left:33px;top:231px" role="img" aria-label="Picture placeholder">PLACE YOUR PICTURE HERE</div>
  <div class="shadow" style="left:38px;top:152px;width:120px"></div>
  <div class="shadow" style="left:38px;top:223px;width:120px"></div>
  <div class="shadow" style="left:38px;top:294px;width:120px"></div>

  <svg class="feature-icon" style="left:185px;top:91px" viewBox="0 0 12 12" aria-hidden="true"><circle cx="6" cy="6" r="5.2" fill="none" stroke="#1b3d5e" stroke-width="1.4"/><path d="M3.4 6.2 L5.3 8 L8.7 4.2" fill="none" stroke="#1b3d5e" stroke-width="1.4"/></svg>
  <p class="body-copy" style="left:185px;top:93px;width:284px;text-indent:24px">Stet clita kasd gubergren, no sea takimata sanctus est Lorem ipsum dolor sit amet. Consetetur labore et dolore dolores et ea rebum.&nbsp; Stet clita kasd gubergren, no sea takimata sanctus est Lorem ipsum dolor sit amet.</p>
  <svg class="feature-icon" style="left:185px;top:162px" viewBox="0 0 12 12" aria-hidden="true"><rect x="1" y="1.5" width="10" height="7" fill="none" stroke="#1b3d5e" stroke-width="1.3"/><path d="M4 11 H8 M6 8.5 V11" stroke="#1b3d5e" stroke-width="1.3"/></svg>
  <p class="body-copy" style="left:185px;top:164px;width:284px;text-indent:24px">Stet clita kasd gubergren, no sea takimata sanctus est Lorem ipsum dolor sit amet. Consetetur labore et dolore dolores et ea rebum.&nbsp; Stet clita kasd gubergren, no sea takimata sanctus est Lorem ipsum dolor sit amet. Stet clita kasd gubergren, no sea takimata sanctus est Lorem ipsum dolor sit amet. Consetetur labore et dolore dolores et ea rebum.&nbsp; Stet clita kasd gubergren, no sea takimata sanctus est Lorem ipsum dolor sit amet.</p>

  <svg class="wave" viewBox="0 0 500 375" aria-hidden="true">
    <defs>
      <linearGradient id="footSea4" x1="0" y1="0" x2="0" y2="1">
        <stop offset="0" stop-color="#1d6fa3"/><stop offset="1" stop-color="#0b3765"/>
      </linearGradient>
    </defs>
    <path d="M0 310 C100 324 200 322 280 304 C360 286 430 270 500 266 L500 375 L0 375Z" fill="url(#footSea4)"/>
  </svg>
  <div class="brand brand--footer" style="top:279px"><span class="brand__dot"></span>vectralink</div>
  <p class="footer-address" style="top:332px">Lorem Ipsum Street 122<br>State, Country<br>Phone&nbsp; 0123 4567 89</p>
  <div class="contact" style="left:113px;top:334px"><span class="contact__icon"><svg viewBox="0 0 8 8"><circle cx="4" cy="4" r="2.2" fill="#fff"/></svg></span>social-one.example/company</div>
  <div class="contact" style="left:113px;top:358px"><span class="contact__icon"><svg viewBox="0 0 8 8"><circle cx="4" cy="4" r="2.8" fill="none" stroke="#fff" stroke-width="1.1"/></svg></span>hello@company-name.com</div>
  <div class="contact" style="left:262px;top:306px"><span class="contact__icon"><svg viewBox="0 0 8 8"><path d="M1 4.2 L4 1.5 L7 4.2 V7 H1Z" fill="#fff"/></svg></span>company-name.com</div>
  <div class="contact" style="left:262px;top:331px"><span class="contact__icon"><svg viewBox="0 0 8 8"><rect x="1.5" y="1.5" width="5" height="5" fill="#fff"/></svg></span>social-two.example/company</div>
  <div class="contact" style="left:262px;top:356px"><span class="contact__icon"><svg viewBox="0 0 8 8"><path d="M2 1.5 L6.5 4 L2 6.5Z" fill="#fff"/></svg></span>video-hub.example/company</div>
  <div class="pager" style="top:341px">
    <span class="pager__btn"><svg viewBox="0 0 6 7"><path d="M5 0.5 L1 3.5 L5 6.5" fill="none" stroke="#fff" stroke-width="1.4"/></svg></span>
    <span>4</span><i>of</i><span>13</span>
    <span class="pager__btn"><svg viewBox="0 0 6 7"><path d="M1 0.5 L5 3.5 L1 6.5" fill="none" stroke="#fff" stroke-width="1.4"/></svg></span>
  </div>
</section>

</body>
</html>
```